Retractable Banner Design for Retail Shopping Event

I need a design for a 33” by 86” retractable banner. It should have my logo at the top (the largest element of the design) and the banner should also include my website and Instagram handle:
www.mirabelhtx.com
@mirabelhtx
I have included product pictures in the brief that can be used. I also included different versions of my logo file, including AI. I need the file to be ready to upload to my printer.
My store is an upscale women’s boutique. I am also attaching designs I have selected in the past to give an idea of my aesthetic.

```html
<!DOCTYPE html>
<html lang="en">
<head>
<meta charset="utf-8">
<title>Mirabel HTX – Retractable Banner</title>
<link href="https://fonts.googleapis.com/css2?family=Montserrat:wght@500;600&family=Dancing+Script:wght@500&display=swap" rel="stylesheet">
<style>
  :root {
    --blush: #f7c9cb;
    --white: #ffffff;
    --ink-grey: #9a9a9a;
    --tote: #d9bfae;
    --tray: #b98e58;
    --slipper: #b9a3b8;
    --earring: #d8b25c;
  }
  html, body {
    margin: 0;
    padding: 0;
    width: 1200px;
    height: 2244px;
    overflow: hidden;
    background: var(--white);
  }
  .banner {
    position: relative;
    width: 1200px;
    height: 2244px;
  }
  .banner-art {
    position: absolute;
    inset: 0;
  }
  .brand-name {
    position: absolute;
    top: 218px;
    left: 0;
    width: 1200px;
    margin: 0;
    text-align: center;
    font-family: "Montserrat", sans-serif;
    font-weight: 600;
    font-size: 68px;
    line-height: 1;
    letter-spacing: 6px;
    color: var(--ink-grey);
  }
  .tagline {
    position: absolute;
    top: 1065px;
    left: 0;
    width: 1200px;
    margin: 0;
    text-align: center;
    font-family: "Dancing Script", cursive;
    font-weight: 500;
    font-size: 84px;
    line-height: 1.2;
    color: var(--ink-grey);
    text-shadow:
      0 0 6px var(--white), 0 0 6px var(--white), 0 0 10px var(--white),
      4px 4px 0 var(--white), -4px -4px 0 var(--white),
      4px -4px 0 var(--white), -4px 4px 0 var(--white),
      0 6px 0 var(--white), 0 -6px 0 var(--white),
      6px 0 0 var(--white), -6px 0 0 var(--white);
  }
  .contact {
    position: absolute;
    top: 1900px;
    left: 0;
    width: 1200px;
    margin: 0;
    text-align: center;
    font-family: "Montserrat", sans-serif;
    font-weight: 500;
    font-size: 47px;
    line-height: 62px;
    letter-spacing: 1px;
    color: var(--ink-grey);
  }
  .contact span { display: block; }
</style>
</head>
<body>
<main class="banner">
  <svg class="banner-art" width="1200" height="2244" viewBox="0 0 1200 2244" xmlns="http://www.w3.org/2000/svg">
    <defs>
      <pattern id="stripe-pattern" x="0" y="0" width="22" height="10" patternUnits="userSpaceOnUse">
        <rect width="22" height="10" fill="#f7c9cb"/>
        <rect x="6" width="11" height="10" fill="#ffffff"/>
      </pattern>
    </defs>

    <rect class="panel" x="203" y="89" width="794" height="2061" fill="var(--blush)"/>
    <rect class="panel-rule" x="218" y="104" width="764" height="2031" fill="none" stroke="var(--white)" stroke-width="3"/>

    <rect class="name-box" x="240" y="129" width="716" height="249" fill="var(--white)"/>
    <rect class="name-box-rule" x="256" y="145" width="684" height="217" fill="none" stroke="var(--blush)" stroke-width="3"/>

    <rect class="stripe-field" x="222" y="398" width="756" height="1402" fill="url(#stripe-pattern)"/>

    <g class="product-diamond">
      <polygon points="388,375 563,550 388,725 213,550" fill="var(--white)"/>
      <polygon points="388,397 541,550 388,703 235,550" fill="none" stroke="var(--blush)" stroke-width="3"/>
      <rect x="323" y="425" width="130" height="190" rx="10" fill="var(--tote)" role="img" aria-label="Blush leather tote bag photo"/>
    </g>
    <g class="product-diamond">
      <polygon points="775,635 950,810 775,985 600,810" fill="var(--white)"/>
      <polygon points="775,657 928,810 775,963 622,810" fill="none" stroke="var(--blush)" stroke-width="3"/>
      <ellipse cx="782" cy="800" rx="130" ry="62" fill="var(--tray)" role="img" aria-label="Leopard print round tray photo"/>
    </g>
    <g class="product-diamond">
      <polygon points="775,1215 950,1390 775,1565 600,1390" fill="var(--white)"/>
      <polygon points="775,1237 928,1390 775,1543 622,1390" fill="none" stroke="var(--blush)" stroke-width="3"/>
      <ellipse cx="775" cy="1390" rx="115" ry="60" fill="var(--slipper)" role="img" aria-label="Lilac pom-pom slippers photo"/>
    </g>
    <g class="product-diamond">
      <polygon points="397,1468 572,1643 397,1818 222,1643" fill="var(--white)"/>
      <polygon points="397,1490 550,1643 397,1796 244,1643" fill="none" stroke="var(--blush)" stroke-width="3"/>
      <rect x="307" y="1603" width="180" height="80" rx="40" fill="var(--earring)" role="img" aria-label="Gold clover stud earrings photo"/>
    </g>

    <rect class="contact-box" x="222" y="1818" width="756" height="290" fill="var(--white)"/>
    <line x1="278" y1="1846" x2="922" y2="1846" stroke="var(--blush)" stroke-width="3"/>
    <line x1="278" y1="1854" x2="922" y2="1854" stroke="var(--blush)" stroke-width="2"/>
    <line x1="278" y1="2058" x2="922" y2="2058" stroke="var(--blush)" stroke-width="3"/>
    <line x1="278" y1="2066" x2="922" y2="2066" stroke="var(--blush)" stroke-width="2"/>
  </svg>

  <h1 class="brand-name">MIRABEL HTX</h1>

  <p class="tagline">Make your life beautiful</p>

  <p class="contact">
    <span class="contact-web">www.MIRABELHTX.com</span>
    <span class="contact-social">@mirabelhtx</span>
  </p>
</main>
</body>
</html>
```